Casa Vero Inspections Business Card

I need a business card for my new company. The company is going to provide home inspections. The name of the company is Casa Vero Inspections. I am not sure if I want a single sided card or a double. I have a logo already that I want to incorporate into the card design. I was wondering if I should incorporate a catch phrase on my card or not. If I did the phrase would be "The Trusted Standard for Home Inspections" but i am unsure how or if to use it on a card. The following information needs to be on the card.
Home Inspection
My Name: Marcus T. Wolford Phone Number: 555-301-7762 Email: mwolford@casaveroinspections.com Website: www.casaveroinspections.com NY HI License # 27300519462

```html
<!DOCTYPE html>
<html lang="en">
<head>
<meta charset="utf-8">
<title>Casa Vero Inspections Business Card</title>
<link href="https://fonts.googleapis.com/css2?family=Montserrat:wght@500;700&family=Roboto:wght@400&display=swap" rel="stylesheet">
<style>
  :root {
    --backdrop: #3a3b3e;
    --card-dark: #1c1c1e;
    --card-light: #f4f4f5;
    --brand-blue: #1f6fb5;
    --sky-blue: #6cc0ef;
    --soft-line: #a9d6f2;
    --ink: #3b3d42;
    --silver: #d9dde2;
  }
  * { box-sizing: border-box; margin: 0; padding: 0; }
  html, body { width: 1200px; height: 900px; overflow: hidden; }
  body {
    background: var(--backdrop);
    position: relative;
    font-family: "Roboto", Arial, sans-serif;
  }
  .card {
    position: absolute;
    width: 640px;
    height: 366px;
    border-radius: 22px;
    overflow: hidden;
  }
  .card-front {
    left: 80px; top: 50px;
    background: var(--card-dark);
    display: flex; flex-direction: column; align-items: center; justify-content: center;
    gap: 22px;
  }
  .front-wordmark {
    display: flex; align-items: center; gap: 14px;
    font-family: "Montserrat", Arial, sans-serif;
    font-weight: 700;
    font-size: 38px;
    letter-spacing: 1px;
    color: var(--sky-blue);
    text-transform: uppercase;
  }
  .wordmark-square { width: 22px; height: 22px; background: var(--sky-blue); }
  .tagline {
    display: flex; align-items: center; gap: 12px;
    color: var(--silver);
    font-size: 14px;
    letter-spacing: 0.5px;
    text-transform: uppercase;
  }
  .tagline-rule { width: 40px; height: 2px; background: var(--sky-blue); }

  .card-back {
    left: 480px; top: 484px;
    background: var(--card-light);
  }
  .back-wordmark {
    position: absolute; right: 40px; top: 60px;
    font-family: "Montserrat", Arial, sans-serif;
    font-weight: 700;
    font-size: 26px;
    color: var(--brand-blue);
    text-transform: uppercase;
    letter-spacing: 0.5px;
  }
  .back-top-rule {
    position: absolute; left: 250px; right: 30px; top: 118px;
    height: 1px; background: var(--soft-line);
  }
  .holder {
    position: absolute; left: 40px; top: 170px;
  }
  .holder-name {
    font-family: "Montserrat", Arial, sans-serif;
    font-weight: 700; font-size: 24px;
    color: var(--brand-blue);
    text-transform: uppercase;
  }
  .holder-title {
    font-family: "Montserrat", Arial, sans-serif;
    font-weight: 500; font-size: 18px;
    color: var(--sky-blue);
    margin-top: 2px;
  }
  .title-rule {
    position: absolute; left: 200px; right: 30px; top: 215px;
    height: 1px; background: var(--soft-line);
  }
  .contact-list {
    position: absolute; left: 40px; top: 262px;
    list-style: none;
    display: flex; flex-direction: column; gap: 6px;
    color: var(--ink); font-size: 16px;
  }
  .contact-list li { display: flex; align-items: center; gap: 10px; }
  .contact-list svg { width: 16px; height: 16px; flex: none; }
  .license {
    position: absolute; right: 40px; top: 262px;
    color: var(--ink); font-size: 16px;
  }
</style>
</head>
<body>
  <section class="card card-front">
    <div class="front-wordmark"><span class="wordmark-square"></span>Casa Vero Inspections</div>
    <div class="tagline"><span class="tagline-rule"></span>The Trusted Standard for Home Inspections<span class="tagline-rule"></span></div>
  </section>

  <section class="card card-back">
    <div class="back-wordmark">Casa Vero Inspections</div>
    <div class="back-top-rule"></div>
    <div class="holder">
      <div class="holder-name">Marcus T. Wolford</div>
      <div class="holder-title">Founder &amp; CEO</div>
    </div>
    <div class="title-rule"></div>
    <ul class="contact-list">
      <li>
        <svg viewBox="0 0 16 16" aria-hidden="true"><path d="M3 1.5l3 .5 1 3-2 1.5c.8 1.8 2.2 3.2 4 4l1.5-2 3 1 .5 3c-1 1-2.5 1.3-4 .8C6.5 12 4 9.5 2.7 5.5 2.2 4 2.5 2.5 3 1.5z" fill="var(--brand-blue)"/></svg>
        555-301-7762
      </li>
      <li>
        <svg viewBox="0 0 16 16" aria-hidden="true"><rect x="1.5" y="3.5" width="13" height="9" fill="none" stroke="var(--brand-blue)" stroke-width="1.5"/><path d="M1.5 3.5L8 9l6.5-5.5" fill="none" stroke="var(--brand-blue)" stroke-width="1.5"/></svg>
        mwolford@casaveroinspections.com
      </li>
      <li>
        <svg viewBox="0 0 16 16" aria-hidden="true"><g fill="none" stroke="var(--brand-blue)" stroke-width="1.2"><circle cx="8" cy="8" r="6.5"/><ellipse cx="8" cy="8" rx="3" ry="6.5"/><path d="M1.5 8h13M2.5 4.8h11M2.5 11.2h11"/></g></svg>
        www.casaveroinspections.com
      </li>
    </ul>
    <div class="license">NY HI License # 27300519462</div>
  </section>
</body>
</html>
```